Brightbuns Business Card Design

Our company is called Brightbuns. We manufacture confectionary snacks & frozen novelties. Our initial product portfolio includes frozen ice lollies/popsicles & stick ice cream bars.

We require a business card design.

Please use the attached Logo.

Please use an orange, brown, yellow colour code. You may choose any combination of the 3 or include all three. The logo however must remain orange.

Target Market(s)

Business card will be targeted at distributors of our products such as supermarket procurement managers, convenience store owners, wholesale distributors and merchandising agents.

Industry/Entity Type

Business

Requirements
Must have
• Kelvin Marsh_Director/ P.O.Box Westhollow 5172, Accra, Ghana / m: 00233(0)507318264/ e: kelvin.marsh@fernpost.co.uk

```html
<!DOCTYPE html>
<html lang="en">
<head>
<meta charset="utf-8">
<title>Brightbuns Business Card Concepts</title>
<link href="https://fonts.googleapis.com/css2?family=Roboto+Condensed:wght@500;700&display=swap" rel="stylesheet">
<style>
  :root {
    --orange: #e8690c;
    --brown: #521810;
    --ink: #4a1a10;
    --paper: #ffffff;
    --edge: #5a5a5a;
  }
  html, body {
    margin: 0;
    padding: 0;
    width: 1200px;
    height: 1000px;
    overflow: hidden;
    background: var(--paper);
  }
  body {
    position: relative;
    font-family: "Roboto Condensed", "Arial Narrow", sans-serif;
  }
  .card {
    position: absolute;
    box-sizing: border-box;
    border: 1px solid var(--edge);
    background: var(--paper);
    overflow: hidden;
  }
  .card svg.backdrop {
    position: absolute;
    inset: 0;
    width: 100%;
    height: 100%;
  }
  .portrait { width: 246px; height: 419px; }
  .portrait.wide-margin { width: 270px; }
  .landscape { width: 419px; height: 271px; }

  .brand {
    position: absolute;
    left: 0;
    right: 0;
    display: flex;
    align-items: center;
    justify-content: center;
    gap: 8px;
    color: var(--orange);
    font-weight: 700;
    font-size: 46px;
    line-height: 1;
    letter-spacing: 0.5px;
  }
  .brand .dot {
    width: 24px;
    height: 24px;
    border-radius: 50%;
    background: var(--orange);
    flex: none;
  }
  .line {
    position: absolute;
    margin: 0;
    font-size: 13px;
    line-height: 16px;
    font-weight: 500;
    text-transform: uppercase;
    white-space: nowrap;
    color: var(--ink);
  }
  .line.centered { left: 0; right: 0; text-align: center; }
  .name { font-weight: 700; font-size: 14px; }
  .role { color: var(--orange); font-weight: 500; }
  .label { color: var(--orange); margin-right: 4px; }
  .on-dark .line { color: #ffffff; }
  .on-dark .role, .on-dark .label { color: var(--orange); }
  .band-text .line { color: #ffffff; }
</style>
</head>
<body>

  <!-- Portrait, plain white -->
  <div class="card portrait wide-margin" style="left:85px; top:64px;">
    <div class="brand" style="top:66px;"><span class="dot"></span>Brightbuns</div>
    <p class="line name" style="left:33px; top:257px;">Kelvin Marsh <span class="role">Director</span></p>
    <p class="line" style="left:33px; top:299px;">P.O.Box Westhollow 5172,</p>
    <p class="line" style="left:33px; top:321px;">Accra, Ghana</p>
    <p class="line" style="left:33px; top:341px;"><span class="label">M</span>00233(0)507318264</p>
    <p class="line" style="left:33px; top:363px;"><span class="label">E</span>kelvin.marsh@fernpost.co.uk</p>
  </div>

  <!-- Portrait, brown arc with orange foot -->
  <div class="card portrait on-dark" style="left:395px; top:65px;">
    <svg class="backdrop" viewBox="0 0 246 419" preserveAspectRatio="none" aria-hidden="true">
      <path d="M0,203 Q140,150 246,170 L246,419 L0,419 Z" fill="var(--brown)"/>
      <path d="M0,393 Q130,408 246,353 L246,419 L0,419 Z" fill="var(--orange)"/>
    </svg>
    <div class="brand" style="top:68px;"><span class="dot"></span>Brightbuns</div>
    <p class="line name" style="left:34px; top:218px;">Kelvin Marsh <span class="role">Director</span></p>
    <p class="line" style="left:34px; top:260px;">P.O.Box Westhollow 5172,</p>
    <p class="line" style="left:34px; top:280px;">Accra, Ghana</p>
    <p class="line" style="left:34px; top:302px;"><span class="label">M</span>00233(0)507318264</p>
    <p class="line" style="left:34px; top:323px;"><span class="label">E</span>kelvin.marsh@fernpost.co.uk</p>
  </div>

  <!-- Landscape, brown contact band -->
  <div class="card landscape" style="left:683px; top:133px;">
    <svg class="backdrop" viewBox="0 0 419 271" preserveAspectRatio="none" aria-hidden="true">
      <rect x="0" y="193" width="419" height="78" fill="var(--brown)"/>
    </svg>
    <div class="brand" style="top:70px;"><span class="dot"></span>Brightbuns</div>
    <p class="line centered name" style="top:168px;">Kelvin Marsh <span class="role">Director</span></p>
    <div class="band-text">
      <p class="line centered" style="top:211px;">P.O.Box Westhollow 5172, Accra, Ghana</p>
      <p class="line centered" style="top:229px;"><span class="label">M</span>00233(0)507318264 <span class="label">E</span>kelvin.marsh@fernpost.co.uk</p>
    </div>
  </div>

  <!-- Landscape, plain white -->
  <div class="card landscape" style="left:99px; top:596px;">
    <div class="brand" style="top:72px;"><span class="dot"></span>Brightbuns</div>
    <p class="line centered name" style="top:168px;">Kelvin Marsh <span class="role">Director</span></p>
    <p class="line centered" style="top:206px;">P.O.Box Westhollow 5172, Accra, Ghana</p>
    <p class="line centered" style="top:224px;"><span class="label">M</span>00233(0)507318264 <span class="label">E</span>kelvin.marsh@fernpost.co.uk</p>
  </div>

  <!-- Portrait, brown dome with orange swoosh -->
  <div class="card portrait on-dark" style="left:567px; top:515px;">
    <svg class="backdrop" viewBox="0 0 246 419" preserveAspectRatio="none" aria-hidden="true">
      <path d="M0,197 Q110,158 246,205 L246,419 L0,419 Z" fill="var(--brown)"/>
      <path d="M0,347 Q90,430 246,400 L246,416 Q90,440 0,366 Z" fill="var(--orange)"/>
    </svg>
    <div class="brand" style="top:76px;"><span class="dot"></span>Brightbuns</div>
    <p class="line name" style="left:35px; top:221px;">Kelvin Marsh <span class="role">Director</span></p>
    <p class="line" style="left:35px; top:263px;">P.O.Box Westhollow 5172,</p>
    <p class="line" style="left:35px; top:284px;">Accra, Ghana</p>
    <p class="line" style="left:35px; top:306px;"><span class="label">M</span>00233(0)507318264</p>
    <p class="line" style="left:35px; top:327px;"><span class="label">E</span>kelvin.marsh@fernpost.co.uk</p>
  </div>

  <!-- Portrait, orange rim over brown dome -->
  <div class="card portrait on-dark" style="left:855px; top:515px;">
    <svg class="backdrop" viewBox="0 0 246 419" preserveAspectRatio="none" aria-hidden="true">
      <path d="M0,206 Q120,160 246,205 L246,226 Q120,180 0,210 Z" fill="var(--orange)"/>
      <path d="M0,210 Q120,180 246,226 L246,419 L0,419 Z" fill="var(--brown)"/>
    </svg>
    <div class="brand" style="top:76px;"><span class="dot"></span>Brightbuns</div>
    <p class="line name" style="left:34px; top:246px;">Kelvin Marsh <span class="role">Director</span></p>
    <p class="line" style="left:34px; top:288px;">P.O.Box Westhollow 5172,</p>
    <p class="line" style="left:34px; top:309px;">Accra, Ghana</p>
    <p class="line" style="left:34px; top:330px;"><span class="label">M</span>00233(0)507318264</p>
    <p class="line" style="left:34px; top:351px;"><span class="label">E</span>kelvin.marsh@fernpost.co.uk</p>
  </div>

</body>
</html>
```